Web design required

1-We need a web design for existing company based in New Zealand
2-We build residential house and light commercial
3-We has in-house designer which allow us can provide interior design
4-We modeling project before site construction, which enable both client and construction team to visually analysis whole project,

Target Market(s)

middle class residential house market
Ref: http://www.brackwellbuilders.co.nz/

Industry/Entity Type

Construction Company

Number of Pages Required

1 page

Font styles to use
Sans Serif
Other font styles liked:
• Such as : Central Gothic or similar which has more design taste

Colors

Designer to choose colors to be used in the design.

Requirements
Must have
• Front sheet, contact information, sample project

```html
<!DOCTYPE html>
<html lang="en">
<head>
<meta charset="utf-8">
<title>Harbourline Homes — Affordable Homes &amp; Apartments</title>
<link rel="stylesheet" href="https://fonts.googleapis.com/css2?family=Cormorant+Garamond:wght@400;500;600&family=Crimson+Text:ital,wght@0,400;0,600;1,400&family=Montserrat:wght@600;700&display=swap">
<style>
  :root{
    --gold:#b39a5a;
    --gold-soft:#c9b27a;
    --paper:#f4f4f4;
    --white:#ffffff;
    --ink:#5d5d5d;
    --muted:#8c8c8c;
    --rule:#d8d2c2;
    --night:#1f2a35;
  }
  *{box-sizing:border-box;margin:0;padding:0}
  html,body{width:1200px;height:3529px;overflow:hidden}
  body{background:var(--paper);font-family:"Crimson Text",Georgia,serif;color:var(--ink);position:relative}
  section,header,footer{position:absolute;left:0;width:1200px}
  .center{position:absolute;left:0;width:1200px;text-align:center}
  .vline{position:absolute;left:599px;width:1px;background:var(--rule)}

  /* Hero */
  .hero{top:0;height:583px;background:linear-gradient(180deg,#2c3947 0%,#4b4a4c 38%,#6a5847 62%,#3a3a34 100%)}
  .hero-photo{position:absolute;inset:0;background:linear-gradient(120deg,rgba(40,52,64,.2) 0%,rgba(120,90,60,.25) 55%,rgba(30,30,28,.4) 100%)}
  .topbar{top:0;height:94px;background:rgba(25,33,42,.75);z-index:2}
  .brand{position:absolute;left:32px;top:28px;display:flex;align-items:center;gap:12px;color:var(--white);font-family:"Montserrat",Arial,sans-serif;font-weight:700;font-size:15px;letter-spacing:3px}
  .brand-mark{width:26px;height:26px;border:2px solid var(--white)}
  .nav{position:absolute;left:430px;top:38px;display:flex;gap:34px;font-family:"Montserrat",Arial,sans-serif;font-weight:700;font-size:10px;letter-spacing:1px;color:var(--white)}
  .nav .active{color:var(--gold-soft)}
  .social-top{position:absolute;right:32px;top:35px;display:flex;gap:12px}
  .social-top span{width:22px;height:22px;border-radius:50%;background:var(--gold)}
  .hero .vline{top:130px;height:94px;background:rgba(255,255,255,.35)}
  .eyebrow{font-family:"Cormorant Garamond",serif;font-size:11px;letter-spacing:4px;text-transform:uppercase}
  .hero .eyebrow{top:226px;color:var(--gold-soft)}
  .hero-title{top:246px;font-family:"Cormorant Garamond",serif;font-weight:500;font-size:35px;line-height:38px;letter-spacing:5px;color:var(--white)}
  .hero-address{top:474px;font-family:"Cormorant Garamond",serif;font-size:12px;letter-spacing:3px;color:rgba(255,255,255,.75)}
  .arrow{position:absolute;top:278px}
  .arrow.left{left:24px}.arrow.right{right:24px}

  /* Intro */
  .intro{top:583px;height:217px;background:linear-gradient(180deg,#ffffff 0%,#f7f7f6 100%)}
  .intro p{position:absolute;left:300px;width:600px;top:70px;text-align:center;font-size:16px;line-height:26px;color:var(--gold)}

  /* Shared section heads */
  .kicker{font-family:"Cormorant Garamond",serif;font-size:12px;letter-spacing:5px;color:var(--muted);text-transform:uppercase}
  .title{font-family:"Cormorant Garamond",serif;font-weight:500;font-size:24px;letter-spacing:6px;color:var(--gold);text-transform:uppercase}
  .lead{position:absolute;left:340px;width:520px;text-align:center;font-size:11.5px;line-height:19px;color:var(--muted)}

  /* Apartments */
  .apartments{top:800px;height:795px;background:var(--paper)}
  .apartments .kicker{top:118px}
  .apartments .title{top:150px}
  .card{position:absolute;top:369px;width:268px}
  .card .photo{height:165px}
  .card h4{margin-top:32px;font-family:"Montserrat",Arial,sans-serif;font-size:8.5px;letter-spacing:1.5px;color:#444;text-transform:uppercase}
  .card p{margin-top:12px;font-size:11.5px;line-height:18px;color:var(--muted)}
  .btn{position:absolute;height:33px;border-radius:17px;font-family:"Montserrat",Arial,sans-serif;font-weight:700;font-size:9px;letter-spacing:1px;display:flex;align-items:center;justify-content:center;text-transform:uppercase}
  .btn.solid{background:var(--gold);color:var(--white)}
  .btn.outline{border:1px solid var(--gold);color:var(--gold)}

  /* Quote band */
  .quote-band{top:1595px;height:339px;background:linear-gradient(90deg,#2b2521 0%,#3b342d 40%,#2a2724 75%,#1e1c1b 100%)}
  .quote-band blockquote{position:absolute;left:330px;width:540px;top:102px;text-align:center;font-style:italic;font-size:19px;line-height:30px;color:var(--white)}
  .play{position:absolute;left:570px;top:182px;width:60px;height:60px;border-radius:50%;background:var(--gold);display:flex;align-items:center;justify-content:center}

  /* Features */
  .features{top:1934px;height:849px;background:var(--paper)}
  .features .kicker{top:120px}
  .features .title{top:150px}
  .amenities{position:absolute;top:378px;left:165px;display:grid;grid-template-columns:228px 230px 229px 200px;row-gap:11px;list-style:none}
  .amenities li{font-size:11px;color:var(--muted);padding-left:28px;position:relative;height:17px}
  .amenities li::before{content:"";position:absolute;left:0;top:4px;width:8px;height:8px;border-radius:50%;background:var(--gold-soft)}
  .gallery{position:absolute;left:393px;top:529px;display:grid;grid-template-columns:repeat(3,136px);grid-auto-rows:82px;gap:4px}

  /* Call to action */
  .cta{top:2783px;height:412px;background:linear-gradient(180deg,#3e4a57 0%,#6b7786 35%,#5d6a57 70%,#8b8a72 100%)}
  .cta .eyebrow{top:166px;color:var(--white);opacity:.85}
  .cta h2{top:198px;font-family:"Crimson Text",serif;font-weight:400;font-size:30px;color:var(--white)}
  .btn.light{background:rgba(255,255,255,.85);color:var(--gold)}

  /* Footer */
  .site-footer{top:3195px;height:334px;background:var(--paper)}
  .footer-col{position:absolute;top:60px}
  .footer-col h5{font-family:"Montserrat",Arial,sans-serif;font-size:9px;letter-spacing:2px;color:#444;text-transform:uppercase;margin-bottom:14px}
  .footer-col p{font-size:12px;line-height:20px;color:var(--muted)}
  .social-foot{position:absolute;left:775px;top:92px;display:flex;gap:12px}
  .social-foot span{width:30px;height:30px;border-radius:50%;background:#c9c9c9}
  .copyright{top:296px;font-size:10px;color:#b0b0b0}
</style>
</head>
<body>

<section class="hero">
  <div class="hero-photo" role="img" aria-label="Timber-clad coastal house at dusk among pine trees"></div>
  <div class="vline"></div>
  <p class="center eyebrow">Welcome to Harbourline Homes</p>
  <h1 class="center hero-title">AFFORDABLE<br>HOMES &amp; APARTMENTS</h1>
  <p class="center hero-address">12 KAURI LANE, AUCKLAND, NZ</p>
  <svg class="arrow left" width="14" height="26" viewBox="0 0 14 26"><path d="M12 2 2 13l10 11" fill="none" stroke="#fff" stroke-width="2.5"/></svg>
  <svg class="arrow right" width="14" height="26" viewBox="0 0 14 26"><path d="M2 2l10 11L2 24" fill="none" stroke="#fff" stroke-width="2.5"/></svg>
</section>

<header class="topbar">
  <div class="brand"><span class="brand-mark"></span>HARBOURLINE HOMES</div>
  <nav class="nav"><span class="active">HOME</span><span>ABOUT</span><span>PORTFOLIO</span><span>SERVICES</span><span>CONTACT</span></nav>
  <div class="social-top"><span></span><span></span></div>
</header>

<section class="intro">
  <p>Welcome to Harbourline Homes, meticulously crafted, designed and constructed to suit your needs, Homes &amp; Apartments, where you can live in your dream home, Without sinking a hole in your pocket.</p>
</section>

<section class="apartments">
  <div class="vline" style="top:35px;height:70px"></div>
  <p class="center kicker">Transforming</p>
  <h2 class="center title">Mordern Apartments</h2>
  <div class="vline" style="top:200px;height:35px"></div>
  <p class="lead" style="top:268px">Every home we build starts as a full model, so you and our site team can walk through each room before the first slab is poured. Our in-house designer shapes interiors that suit the way you live, on budget.</p>

  <article class="card" style="left:160px">
    <div class="photo" role="img" aria-label="Brick neo-classic house with gabled roof" style="background:linear-gradient(180deg,#c9d3dc 0%,#7a5a48 55%,#4a3a30 100%)"></div>
    <h4>Neo Classic Design</h4>
    <p>Brick facades and steep gable roofs bring timeless character, paired with modern insulation and open living spaces.</p>
  </article>
  <article class="card" style="left:466px">
    <div class="photo" role="img" aria-label="Aerial view of a home surrounded by green lawns and gardens" style="background:linear-gradient(135deg,#3d5a32 0%,#5f7d44 50%,#2f4527 100%)"></div>
    <h4>Loads of Green Space</h4>
    <p>Generous lawns and planted courtyards give every family room to play, relax and grow their own garden.</p>
  </article>
  <article class="card" style="left:772px">
    <div class="photo" role="img" aria-label="Warmly lit timber interior with large windows" style="background:linear-gradient(135deg,#2e261e 0%,#7a5534 50%,#3a3b2e 100%)"></div>
    <h4>Earthly Vibes</h4>
    <p>Warm timber, soft lighting and natural textures create calm interiors you will love coming home to.</p>
  </article>

  <div class="btn solid" style="left:541px;top:692px;width:118px">Floor Plans</div>
</section>

<section class="quote-band" role="img" aria-label="Dim living room with fireplace and shelving">
  <blockquote>"Carefully Crafted Design, with a great level of attention paid to every single detail. After all the devil lives in the detail."</blockquote>
  <div class="play"><svg width="14" height="16" viewBox="0 0 14 16"><path d="M2 1l11 7-11 7z" fill="#fff"/></svg></div>
</section>

<section class="features">
  <div class="vline" style="top:66px;height:47px"></div>
  <p class="center kicker">Modern</p>
  <h2 class="center title">Features &amp; Ameneties</h2>
  <div class="vline" style="top:197px;height:47px"></div>
  <p class="lead" style="top:268px">Every apartment comes with the comforts middle-class families expect, from secure parking to reliable backup power, so daily life runs smoothly while you enjoy a home built to last for decades.</p>

  <ul class="amenities">
    <li>Covered Car park</li><li>Covered Car park</li><li>Covered Car park</li><li>Swimming Pool</li>
    <li>Power Backup</li><li>Power Backup</li><li>Power Backup</li><li>Power Backup</li>
    <li>24/7 Advanced Security</li><li>24/7 Advanced Security</li><li>24/7 Advanced Security</li><li>24/7 Advanced Security</li>
  </ul>

  <div class="gallery">
    <div role="img" aria-label="Swimming pool with blue water" style="background:linear-gradient(180deg,#5fb6d6,#2f87b0)"></div>
    <div role="img" aria-label="Hillside homes among trees" style="background:linear-gradient(180deg,#7d8c7a,#4b5a3e)"></div>
    <div role="img" aria-label="Brick street with townhouses" style="background:linear-gradient(180deg,#6b5a4c,#8a4e3a)"></div>
    <div role="img" aria-label="Lit pool deck at twilight" style="background:linear-gradient(180deg,#3c4a5c,#8a6b4a)"></div>
    <div role="img" aria-label="Resort pool with lights at night" style="background:linear-gradient(180deg,#1f2a3a,#6a5a3a)"></div>
    <div role="img" aria-label="Timber house with pool at dusk" style="background:linear-gradient(180deg,#4a3a32,#a0643a)"></div>
  </div>

  <div class="btn outline" style="left:546px;top:744px;width:108px">Portfolio</div>
</section>

<section class="cta" role="img" aria-label="Lake and mountain landscape with reeds">
  <p class="center eyebrow">It's time for you</p>
  <h2 class="center">Live a life of abundant happiness</h2>
  <div class="btn light" style="left:498px;top:263px;width:76px">Call Us</div>
  <div class="btn light" style="left:595px;top:263px;width:95px">Email Us</div>
</section>

<footer class="site-footer">
  <div class="footer-col" style="left:94px;width:300px">
    <h5>About</h5>
    <p>Harbourline Homes builds residential houses and light commercial projects across Auckland, with design and modelling done in-house.</p>
  </div>
  <div class="footer-col" style="left:470px;width:260px">
    <h5>Contact</h5>
    <p>Ph: +64 (09) 555 0142<br>hello@harbourlinehomes.co.nz<br>12 Kauri Lane, Auckland, NZ</p>
  </div>
  <div class="social-foot"><span></span><span></span><span></span></div>
  <p class="center copyright">Copyright © Harbourline Homes 2024. All rights reserved.</p>
</footer>

</body>
</html>
```